A Speech Therapy Business needs to update their logo

I need an update to the font and color of my logo to look more appealing. I am looking to open a private practice as a Speech Language Pathologist that caters to adults and children. It needs to be sophisticated and friendly at the same time. I want to keep the silhouette in my logo as is, just update the font and color for "Brightpaths".
Industry/Entity Type
Business
Contact Information for Business Card
I want the business card to have my logo, my name (Dorota Valk, CCC-SLP, TSSLD) and that I am a Bilingual Speech Language Pathologist. Also, include my phone number, (555) 271-8390. Include my website, Brightpathsslp.example, and email address, dorotavalk@brightpathsslp.example
Look and feel
Each slider illustrates characteristics of the customer's brand and the style your logo design should communicate.

```html
<!DOCTYPE html>
<html lang="en">
<head>
<meta charset="utf-8">
<title>Brightpaths – Business Card</title>
<link href="https://fonts.googleapis.com/css2?family=Open+Sans:wght@400;600;700&display=swap" rel="stylesheet">
<style>
  :root {
    --backdrop: #e9ecef;
    --card: #ffffff;
    --brand-blue: #1a84c4;
    --brand-orange: #e0621f;
    --ink: #4a4a4a;
    --ink-soft: #555555;
    --icon-blue: #3a8fd0;
    --figure-dark: #2a2a2a;
  }
  * { margin: 0; padding: 0; box-sizing: border-box; }
  html, body {
    width: 1200px;
    height: 1000px;
    overflow: hidden;
    background: var(--backdrop);
    font-family: "Open Sans", Arial, sans-serif;
  }
  .business-card {
    position: absolute;
    left: 100px;
    top: 214px;
    width: 1000px;
    height: 571px;
    background: var(--card);
    overflow: hidden;
    box-shadow: 0 10px 30px rgba(0,0,0,0.15);
  }
  .card-swoosh {
    position: absolute;
    left: 0;
    top: 0;
    width: 1000px;
    height: 571px;
  }
  .name-marker {
    position: absolute;
    left: 45px;
    top: 60px;
    width: 18px;
  }
  .name-marker .marker-blue { height: 24px; background: var(--brand-blue); }
  .name-marker .marker-orange { height: 24px; background: var(--brand-orange); }
  .holder-name {
    position: absolute;
    left: 82px;
    top: 52px;
    font-size: 37px;
    font-weight: 700;
    line-height: 1.2;
    color: var(--ink);
    letter-spacing: 0.3px;
  }
  .holder-name .surname { color: var(--brand-orange); }
  .credentials {
    position: absolute;
    left: 82px;
    top: 100px;
    font-size: 21px;
    font-weight: 600;
    line-height: 1.3;
    color: var(--ink-soft);
    letter-spacing: 0.5px;
  }
  .job-title {
    position: absolute;
    left: 82px;
    top: 131px;
    font-size: 17px;
    font-weight: 400;
    line-height: 1.3;
    color: var(--ink-soft);
  }
  .contact-list {
    position: absolute;
    left: 588px;
    top: 38px;
    list-style: none;
  }
  .contact-list li {
    display: flex;
    align-items: center;
    height: 33px;
    font-size: 19px;
    color: var(--ink-soft);
  }
  .contact-list svg {
    width: 20px;
    height: 20px;
    margin-right: 14px;
    flex: none;
  }
  .brand-lockup {
    position: absolute;
    left: 590px;
    top: 285px;
    width: 360px;
  }
  .brand-figures {
    width: 355px;
    height: 108px;
    background: linear-gradient(90deg, #3a3a3a, #4a4a4a 70%, #6a6a6a);
    opacity: 0.8;
    border-radius: 4px;
  }
  .brand-name {
    margin-top: 10px;
    margin-left: 12px;
    font-size: 44px;
    font-weight: 600;
    color: var(--ink);
    line-height: 1.1;
  }
</style>
</head>
<body>
  <div class="business-card">
    <svg class="card-swoosh" viewBox="0 0 1000 571" aria-hidden="true">
      <path d="M0,160 Q320,430 880,571 L0,571 Z" fill="var(--brand-blue)"/>
      <path d="M0,146 Q320,416 900,571" fill="none" stroke="var(--brand-orange)" stroke-width="7"/>
    </svg>

    <div class="name-marker">
      <div class="marker-blue"></div>
      <div class="marker-orange"></div>
    </div>
    <h1 class="holder-name">Dorota <span class="surname">Valk</span></h1>
    <p class="credentials">CCC-SLP,TSSLD</p>
    <p class="job-title">Bilingual Speech Language Pathologist</p>

    <ul class="contact-list">
      <li>
        <svg viewBox="0 0 20 20" aria-hidden="true"><rect x="5" y="1.5" width="10" height="17" rx="2" fill="none" stroke="var(--icon-blue)" stroke-width="1.8"/><line x1="8.5" y1="15.5" x2="11.5" y2="15.5" stroke="var(--icon-blue)" stroke-width="1.6"/></svg>
        (555)271-8390
      </li>
      <li>
        <svg viewBox="0 0 20 20" aria-hidden="true"><rect x="2" y="4.5" width="16" height="11" fill="none" stroke="var(--icon-blue)" stroke-width="1.6"/><path d="M2,4.5 L10,11 L18,4.5" fill="none" stroke="var(--icon-blue)" stroke-width="1.6"/></svg>
        dorotavalk@brightpathsslp.example
      </li>
      <li>
        <svg viewBox="0 0 20 20" aria-hidden="true"><circle cx="10" cy="10" r="8" fill="none" stroke="var(--icon-blue)" stroke-width="1.6"/><ellipse cx="10" cy="10" rx="3.5" ry="8" fill="none" stroke="var(--icon-blue)" stroke-width="1.4"/><line x1="2" y1="10" x2="18" y2="10" stroke="var(--icon-blue)" stroke-width="1.4"/></svg>
        www.brightpathsslp.example
      </li>
    </ul>

    <div class="brand-lockup">
      <div class="brand-figures" role="img" aria-label="Silhouette illustration of a family walking hand in hand, from adults to a small child, ending in a small heart"></div>
      <p class="brand-name">Brightpaths</p>
    </div>
  </div>
</body>
</html>
```